Brackenfold Cider Works needs web page design

Need a web design for a ecommerce website for honey wine. We make honeywine (a dessert type wine made with honey). Our initial product is a standard honey wine and pyment and a cyser. We have all our logos and designs but need to place in web design to reflect our product and ecommerce. We want the file labeled "facebook cover logo 2" as the banner for the site.

Target Market(s)

People who drink sweeter wines, dessert wine, or non traditional/non-grape wines. Cizer drinkers. 20-60 years old.

Requirements
Must have
• The "bee button" picture as the button image. The "fb cover 2" image as the page banner. Open, bright feel/coloring. Coloring featuring gold, red colors that reflect our logos. PLEASE USE THE FACEBOOK COVER 2 AS OR ON LABEL BANNER TOP OF WEB PAGE. Files 2-3-4 and 5 are our first labels. Those are what will be on bottles when we sale them. This should reflect on web page. We will not use file 8 labels but the graphics could be used on website. There for inspiration.
Nice to have
• Reflect the fonts that are on our logos as close as possible.
Should not have
• Not too much black, red, or honey references. We don't want the page to be too saturated with any of those elements. Not cluttered with imagery.

```html
<!DOCTYPE html>
<html lang="en">
<head>
<meta charset="utf-8">
<title>Brackenfold Cider Works</title>
<link rel="stylesheet" href="https://fonts.googleapis.com/css2?family=Prata&family=Roboto:wght@400;500&display=swap">
<style>
:root{
  --maroon:#8b1030;
  --maroon-dark:#7d0d29;
  --gold:#e9a11c;
  --gold-soft:#c9a24a;
  --ink:#2b2b2b;
  --body:#555;
  --sand:#f4f1ec;
  --white:#fff;
  --serif:'Prata', Georgia, serif;
  --sans:'Roboto', Arial, sans-serif;
}
*{box-sizing:border-box;margin:0;padding:0}
html,body{width:1200px;height:3787px;overflow:hidden}
body{position:relative;background:var(--white);font-family:var(--sans);color:var(--ink)}
.abs{position:absolute}

/* header */
.site-header{position:absolute;left:0;top:0;width:1200px;height:125px;background:var(--white)}
.brand{position:absolute;left:113px;top:34px;display:flex;align-items:center;gap:10px}
.brand-dot{width:14px;height:14px;border-radius:50%;background:var(--maroon)}
.brand-name{font-family:var(--serif);color:var(--maroon);font-size:22px;line-height:27px;letter-spacing:2px;text-transform:uppercase;white-space:nowrap}
.main-nav{position:absolute;top:58px;left:0;width:1200px}
.main-nav a{position:absolute;font-family:var(--serif);font-size:13px;color:var(--ink);text-decoration:none;white-space:nowrap}
.main-nav a.active{color:var(--maroon)}
.cart{position:absolute;left:1039px;top:41px;width:48px;height:48px;border:2px solid var(--maroon);border-radius:50%}
.cart-count{position:absolute;left:0;top:5px;width:44px;text-align:center;font-size:11px;color:var(--ink)}

/* hero */
.hero{position:absolute;left:0;top:125px;width:1200px;height:760px;
  background:radial-gradient(circle at 12% 22%,#f6d68a 0,#d89a3f 18%,transparent 40%),
  linear-gradient(100deg,#8a5a22 0%,#b98236 30%,#6e4618 55%,#3e2710 80%,#5a3a16 100%)}
.hero-wave{position:absolute;left:0;bottom:0;width:1200px;height:140px}
.hero-title{position:absolute;left:157px;top:300px;font-family:var(--serif);font-size:62px;line-height:78px;font-weight:400;color:var(--white);text-shadow:0 2px 6px rgba(0,0,0,.35);white-space:nowrap}

/* pill button */
.pill{position:absolute;height:58px;border-radius:29px;background:var(--maroon);color:var(--white);
  font-family:var(--serif);font-size:16px;display:flex;align-items:center;padding-left:22px;text-transform:uppercase;white-space:nowrap}
.pill-coin{position:absolute;right:4px;top:5px;width:48px;height:48px;border-radius:50%;
  background:radial-gradient(circle at 35% 35%,#f1d98a,#c9a24a 60%,#8e6d22)}

/* welcome */
.welcome-art{position:absolute;left:111px;top:945px;width:476px;height:546px;
  background:linear-gradient(180deg,#2c2c2c,#1d1d1d 85%,#3a3a3a)}
.eyebrow{font-family:var(--serif);color:var(--maroon);font-size:25px;white-space:nowrap}
.section-title{font-family:var(--serif);color:var(--gold);font-size:27px;font-weight:400;white-space:nowrap}
.copy{font-size:13px;line-height:26px;color:var(--body);text-align:justify}

/* products */
.products{position:absolute;left:0;top:1572px;width:1200px;height:650px;background:var(--sand)}
.center-title{position:absolute;left:0;width:1200px;text-align:center;font-family:var(--serif);font-size:36px;font-weight:400;color:var(--maroon)}
.center-title span{color:var(--gold)}
.rule{position:absolute;left:574px;width:52px;height:3px;background:var(--maroon)}
.product-card{position:absolute;top:132px;width:311px;height:449px;background:var(--white);box-shadow:0 2px 8px rgba(0,0,0,.08)}
.bottle{position:absolute;left:112px;top:28px;width:88px;height:285px;border-radius:30px 30px 12px 12px}
.price{position:absolute;left:0;top:336px;width:100%;text-align:center;font-family:var(--serif);font-size:21px;color:var(--maroon)}
.product-name{position:absolute;left:0;top:366px;width:100%;text-align:center;font-family:var(--serif);font-size:20px;color:var(--ink)}
.stars{position:absolute;left:0;top:395px;width:100%;text-align:center;color:var(--gold);font-size:16px;letter-spacing:3px}

/* feature */
.feature{position:absolute;left:0;top:2222px;width:1200px;height:533px;
  background:linear-gradient(90deg,#c9a37a 0%,#d9c0a2 35%,#efe3d4 55%,#f4ece1 100%)}
.feature-title{position:absolute;left:602px;top:122px;font-family:var(--serif);font-size:29px;font-weight:400;color:var(--maroon);white-space:nowrap}
.feature-sub{position:absolute;left:602px;top:171px;font-family:var(--serif);font-size:20px;color:var(--ink);white-space:nowrap}

/* blog */
.blog-card{position:absolute;top:2896px;width:313px;height:405px;background:var(--white);box-shadow:0 2px 8px rgba(0,0,0,.1)}
.blog-photo{width:313px;height:242px}
.blog-title{position:absolute;left:21px;top:262px;width:280px;font-family:var(--serif);font-size:14px;line-height:26px;font-weight:400;color:var(--ink)}
.blog-meta{position:absolute;left:21px;top:331px;font-family:var(--serif);font-size:12px;color:#666;display:flex;gap:22px;white-space:nowrap}
.blog-meta span{display:flex;align-items:center;gap:5px}
.blog-more{position:absolute;left:21px;top:362px;font-family:var(--serif);font-size:13px;color:var(--gold);text-decoration:underline}

/* footer */
.site-footer{position:absolute;left:0;top:3388px;width:1200px;height:399px;background:var(--maroon);color:var(--white)}
.footer-brand{position:absolute;left:110px;top:102px;width:286px;text-align:center;font-family:var(--serif);font-size:22px;line-height:32px;letter-spacing:3px;text-transform:uppercase}
.socials{position:absolute;left:146px;top:222px;display:flex;gap:6px}
.socials i{display:block;width:37px;height:37px;border:2px solid var(--white);border-radius:50%}
.footer-head{position:absolute;top:99px;font-family:var(--serif);font-size:16px;letter-spacing:.5px}
.quick-links{position:absolute;left:426px;top:135px;list-style:none;font-size:13px;line-height:28px}
.quick-links li::before{content:"\2192";margin-right:18px}
.contact-item{position:absolute;left:612px;display:flex;align-items:flex-start;gap:14px;font-size:13px;line-height:24px}
.contact-icon{flex:none;width:34px;height:34px;border-radius:50%;background:var(--maroon-dark);border:1px solid #a22a48;display:flex;align-items:center;justify-content:center}
.newsletter-text{position:absolute;left:872px;top:138px;width:230px;font-size:13px;line-height:20px}
.newsletter-input{position:absolute;left:872px;top:195px;width:216px;height:39px;background:var(--white);color:#555;font-size:12px;padding:12px 14px}
.submit{position:absolute;left:872px;top:253px;width:85px;height:31px;background:var(--gold);color:var(--white);font-size:11px;font-weight:500;text-align:center;line-height:31px}
.copyright{position:absolute;left:0;top:355px;width:1200px;text-align:center;font-size:15px}
</style>
</head>
<body>

<header class="site-header">
  <div class="brand">
    <span class="brand-dot"></span>
    <div class="brand-name">Brackenfold<br>Cider Works</div>
  </div>
  <nav class="main-nav">
    <a class="active" style="left:495px">HOME</a>
    <a style="left:592px">ABOUT US</a>
    <a style="left:715px">PRODUCTS</a>
    <a style="left:843px">NEWS</a>
    <a style="left:938px">CONTACT US</a>
  </nav>
  <div class="cart">
    <div class="cart-count">0</div>
    <svg class="abs" style="left:13px;top:19px" width="18" height="16" viewBox="0 0 18 16"><path d="M0 1h3l3 9h9l2-7H5" fill="none" stroke="#8b1030" stroke-width="2"/><circle cx="7" cy="14" r="1.6" fill="#8b1030"/><circle cx="14" cy="14" r="1.6" fill="#8b1030"/></svg>
  </div>
</header>

<section class="hero" role="img" aria-label="Two glasses of golden honey wine on a table at sunset with grapes">
  <h1 class="hero-title">BRACKENFOLD<br>CIDER WORKS</h1>
  <div class="pill" style="left:155px;top:485px;width:185px">Read more<span class="pill-coin"></span></div>
  <svg class="hero-wave" viewBox="0 0 1200 140" preserveAspectRatio="none"><path d="M0 70 C20 40 40 40 60 60 C80 80 90 130 120 130 C150 130 150 70 190 70 C230 70 250 80 290 60 C330 40 360 70 400 90 C430 105 450 60 490 60 C530 60 560 90 600 75 C640 60 660 30 700 50 C730 65 740 110 770 110 C800 110 810 50 860 45 C900 40 900 80 940 70 C980 60 990 20 1030 30 C1060 40 1070 130 1110 130 C1150 130 1170 60 1200 40 L1200 140 L0 140 Z" fill="#fff"/></svg>
</section>

<div class="welcome-art" role="img" aria-label="Honey wine label artwork on a dark honeycomb background"></div>
<div class="eyebrow abs" style="left:641px;top:1006px">WELCOME TO</div>
<h2 class="section-title abs" style="left:641px;top:1047px">BRACKENFOLD CIDER WORKS</h2>
<p class="copy abs" style="left:641px;top:1106px;width:448px">Sed ut perspiciatis unde omnis iste natus error sit voluptatem accusantium doloremque laudantium, totam rem aperiam, eaque ipsa quae ab illo inventore veritatis et quasi architecto beatae vitae dicta sunt explicabo. Nemo enim ipsam voluptatem quia voluptas sit aspernatur aut odit aut fugit, sed quia consequuntur magni dolores eos qui ratione voluptatem sequi nesciunt. Neque porro quisquam est, qui dolorem ipsum quia dolor sit amet, consectetur, adipisci velit, sed quia non numquam eius modi tem abore et dolore magnam aliquam quaerat voluptatem.</p>
<div class="pill" style="left:641px;top:1343px;width:191px">Read more<span class="pill-coin"></span></div>

<section class="products">
  <h2 class="center-title" style="top:40px">OUR <span>PRODUCTS</span></h2>
  <div class="rule" style="top:96px"></div>
  <article class="product-card" style="left:111px">
    <div class="bottle" role="img" aria-label="Bottle of red honey wine" style="background:linear-gradient(90deg,#1a0a0e,#3a1420 50%,#140608)"></div>
    <div class="price">$25.99</div><div class="product-name">PRODUCT NAME</div><div class="stars">★★★★★</div>
  </article>
  <article class="product-card" style="left:444px">
    <div class="bottle" role="img" aria-label="Bottle of rosé honey wine" style="background:linear-gradient(90deg,#c9745a,#eaa88a 50%,#b8624a)"></div>
    <div class="price">$25.99</div><div class="product-name">PRODUCT NAME</div><div class="stars">★★★★★</div>
  </article>
  <article class="product-card" style="left:777px">
    <div class="bottle" role="img" aria-label="Bottle of golden honey wine" style="background:linear-gradient(90deg,#b8b02e,#e6df7a 50%,#a39a22)"></div>
    <div class="price">$25.99</div><div class="product-name">PRODUCT NAME</div><div class="stars">★★★★★</div>
  </article>
</section>

<section class="feature">
  <div class="abs" role="img" aria-label="Honey wine bottle with bread, garlic and cheese on a stone table" style="left:0;top:0;width:600px;height:533px;background:linear-gradient(90deg,#b89068 0%,#a37a52 40%,rgba(217,192,162,0) 100%)"></div>
  <h2 class="feature-title">SED UT PERSPICIATIS</h2>
  <div class="feature-sub">OMNIS ISTE NATUS ERROR SIT VOLUPTATEM</div>
  <p class="copy abs" style="left:605px;top:208px;width:485px;text-align:left">Nemo enim ipsam voluptatem quia voluptas sit aspernatur aut odit aut fugitsed quia consequuntur magni dolores eos qui ratione voluptatem sequi nesciunt Ne que porro quisquam est, qui dolorem ipsum quia dolsit amet, consectet adipisci velit, sed quia non numquam eius</p>
  <div class="pill" style="left:605px;top:350px;width:190px">Learn more<span class="pill-coin"></span></div>
</section>

<h2 class="center-title" style="top:2800px">LATEST <span>BLOG</span></h2>
<div class="rule" style="top:2857px"></div>

<article class="blog-card" style="left:111px">
  <div class="blog-photo" role="img" aria-label="Wine bottle with cheese and grapes on a dark table" style="background:linear-gradient(135deg,#3a2a1c,#6a5030 45%,#1c2430)"></div>
  <h3 class="blog-title">SED UT PERSPICIATIS UNDE OMNIS ISTE NATUS ERROR SIT</h3>
  <div class="blog-meta"><span><svg width="11" height="11" viewBox="0 0 11 11"><rect x=".5" y="1.5" width="10" height="9" fill="none" stroke="#777"/><path d="M.5 4h10" stroke="#777"/></svg>October 28, 2021</span><span><svg width="11" height="10" viewBox="0 0 11 10"><path d="M1 1h9v6H4L1 9z" fill="none" stroke="#777"/></svg>0 Comments</span></div>
  <a class="blog-more">READ MORE</a>
</article>
<article class="blog-card" style="left:444px">
  <div class="blog-photo" role="img" aria-label="Glasses of white wine and a honey jar on a wooden table" style="background:linear-gradient(135deg,#4a3a24,#8a6a3c 50%,#2e2418)"></div>
  <h3 class="blog-title">SED UT PERSPICIATIS UNDE OMNIS ISTE NATUS ERROR SIT</h3>
  <div class="blog-meta"><span><svg width="11" height="11" viewBox="0 0 11 11"><rect x=".5" y="1.5" width="10" height="9" fill="none" stroke="#777"/><path d="M.5 4h10" stroke="#777"/></svg>October 28, 2021</span><span><svg width="11" height="10" viewBox="0 0 11 10"><path d="M1 1h9v6H4L1 9z" fill="none" stroke="#777"/></svg>0 Comments</span></div>
  <a class="blog-more">READ MORE</a>
</article>
<article class="blog-card" style="left:776px">
  <div class="blog-photo" role="img" aria-label="Wine bottles and glasses on a dark surface with a striped cloth" style="background:linear-gradient(135deg,#1e2228,#3a3c40 50%,#6a6a5a)"></div>
  <h3 class="blog-title">SED UT PERSPICIATIS UNDE OMNIS ISTE NATUS ERROR SIT</h3>
  <div class="blog-meta"><span><svg width="11" height="11" viewBox="0 0 11 11"><rect x=".5" y="1.5" width="10" height="9" fill="none" stroke="#777"/><path d="M.5 4h10" stroke="#777"/></svg>October 28, 2021</span><span><svg width="11" height="10" viewBox="0 0 11 10"><path d="M1 1h9v6H4L1 9z" fill="none" stroke="#777"/></svg>0 Comments</span></div>
  <a class="blog-more">READ MORE</a>
</article>

<footer class="site-footer">
  <div class="footer-brand">Brackenfold<br>Cider Works</div>
  <div class="socials"><i></i><i></i><i></i><i></i><i></i></div>

  <div class="footer-head" style="left:426px">QUICK LINKS</div>
  <ul class="quick-links"><li>HOME</li><li>ABOUT US</li><li>PRODUCTS</li><li>NEWS</li><li>CONTACT US</li></ul>

  <div class="footer-head" style="left:615px">CONTACT</div>
  <div class="contact-item" style="top:136px"><span class="contact-icon"><svg width="13" height="13" viewBox="0 0 13 13"><path d="M2 1l3 0 1 3-2 1c1 2 2 3 4 4l1-2 3 1 0 3c-6 0-10-4-10-10z" fill="#fff"/></svg></span><span style="padding-top:5px">000-121-1231</span></div>
  <div class="contact-item" style="top:185px"><span class="contact-icon"><svg width="13" height="10" viewBox="0 0 13 10"><rect x=".5" y=".5" width="12" height="9" fill="none" stroke="#fff"/><path d="M.5 .5l6 5 6-5" fill="none" stroke="#fff"/></svg></span><span style="padding-top:5px">info@companyname.com</span></div>
  <div class="contact-item" style="top:234px"><span class="contact-icon"><svg width="10" height="14" viewBox="0 0 10 14"><path d="M5 0a5 5 0 0 1 5 5c0 4-5 9-5 9S0 9 0 5a5 5 0 0 1 5-5z" fill="#fff"/><circle cx="5" cy="5" r="1.8" fill="#8b1030"/></svg></span><span>#2154 lorem ipsum dummy<br>lorem dummy</span></div>

  <div class="footer-head" style="left:872px">NEWSLETTER</div>
  <p class="newsletter-text">Sed ut perspiciatis unde omnis us error sit voluptatem</p>
  <div class="newsletter-input">Email :</div>
  <div class="submit">SUBMIT</div>

  <p class="copyright">© Copyrights 2021 Brackenfold Cider Works.All Rights Reserved.</p>
</footer>

</body>
</html>
```